Ardenwell Building and Property Services needs a business card design

We need a business card design for our building and property services business. We already have a logo we just need a creative design and layout on a business card. Emphasis on clean, modern, professional.
Our client targets are mainly body corporates, building managers, construction managers.
We are a building services company that lean more to structural repair of buildings, through concrete rectification and carbon fibre strengthening.
We also refurbish facades, rendering, painting etc
We target higher end body corporates in prestigious locations, hence why we'd like our cards to reflect professionalism, strength, efficiency

Target Market(s)

body corporates, building managers, construction managers

Industry/Entity Type

Construction

Contact Information for Business Card

Ardenwell is the main word, with 'Building and Property Services' underneath.
Level 17, 82 Harlow Street
MERRIDALE
Melbourne
Vic 3094
T: 9518 2736
Duncan Ferris - Director
dunardenwell@mailbox-example.com

Requirements
Must have
• Stand out on the back of the card- strong/ bold, company logo
• All of the contact details written above
Should not have
• I'd like the card to stand out, especially on the back. Id like the company logo to be prominent, although feel free to be creative around it. But remain clean and professional

```html
<!DOCTYPE html>
<html lang="en">
<head>
<meta charset="utf-8">
<title>Ardenwell Building and Property Services – Business Card</title>
<link rel="stylesheet" href="https://fonts.googleapis.com/css2?family=Montserrat:wght@400;500&display=swap">
<style>
  :root {
    --stage: #e9ebee;
    --card: #ffffff;
    --navy: #1b4e93;
    --sky: #2ea6dc;
    --steel: #a7a9ac;
    --text-grey: #8a8c90;
    --shadow: rgba(20, 30, 50, 0.18);
  }
  * { box-sizing: border-box; margin: 0; padding: 0; }
  html, body {
    width: 1200px;
    height: 900px;
    overflow: hidden;
    background: var(--stage);
    font-family: "Montserrat", sans-serif;
  }
  .stage {
    width: 1200px;
    height: 900px;
    display: flex;
    flex-direction: column;
    align-items: center;
    justify-content: center;
    gap: 56px;
  }
  .card {
    position: relative;
    width: 640px;
    height: 366px;
    background: var(--card);
    box-shadow: 0 10px 30px var(--shadow);
    overflow: hidden;
  }
  .edge-band {
    position: absolute;
    top: 0;
    bottom: 0;
    width: 70px;
  }
  .card-front .edge-band { left: 0; }
  .card-back .edge-band { right: 0; }

  /* Front: brand name */
  .brand {
    position: absolute;
    color: var(--navy);
    font-weight: 500;
    text-transform: uppercase;
  }
  .card-front .brand {
    left: 240px;
    top: 135px;
    display: flex;
    align-items: center;
    gap: 16px;
  }
  .brand-square {
    width: 34px;
    height: 34px;
    background: var(--navy);
    flex: none;
  }
  .brand-name {
    display: block;
    font-size: 40px;
    letter-spacing: 4px;
    line-height: 1;
  }
  .brand-tagline {
    display: block;
    font-size: 10.5px;
    letter-spacing: 2.6px;
    margin-top: 8px;
  }

  /* Back: contact details */
  .card-back .brand { left: 48px; top: 60px; }
  .card-back .brand-name { font-size: 36px; letter-spacing: 3.6px; }
  .card-back .brand-tagline { font-size: 9.5px; letter-spacing: 2.4px; }

  .person {
    position: absolute;
    left: 48px;
    top: 168px;
  }
  .person-name {
    font-size: 20px;
    font-weight: 500;
    color: var(--navy);
    text-transform: uppercase;
    letter-spacing: 0.5px;
  }
  .person-name .surname { color: var(--sky); }
  .person-role {
    font-size: 12px;
    color: var(--text-grey);
    margin-top: 2px;
  }
  .contact-list {
    list-style: none;
    margin-top: 12px;
    font-size: 13px;
    color: var(--text-grey);
    line-height: 1.55;
  }
  .contact-list li { display: flex; align-items: center; gap: 8px; }
  .contact-list svg { width: 12px; height: 12px; flex: none; fill: var(--navy); }
  .address {
    margin-top: 8px;
    font-size: 13px;
    font-style: normal;
    color: var(--text-grey);
    line-height: 1.45;
  }
</style>
</head>
<body>
<main class="stage">

  <section class="card card-front" aria-label="Card front">
    <svg class="edge-band" viewBox="0 0 70 366" preserveAspectRatio="none" aria-hidden="true">
      <rect x="0" y="0" width="46" height="366" fill="var(--navy)"/>
      <rect x="52" y="0" width="12" height="366" fill="var(--steel)"/>
    </svg>
    <div class="brand">
      <span class="brand-square" aria-hidden="true"></span>
      <div>
        <span class="brand-name">Ardenwell</span>
        <span class="brand-tagline">Building and Property Services</span>
      </div>
    </div>
  </section>

  <section class="card card-back" aria-label="Card back">
    <svg class="edge-band" viewBox="0 0 70 366" preserveAspectRatio="none" aria-hidden="true">
      <rect x="6" y="0" width="12" height="366" fill="var(--steel)"/>
      <rect x="24" y="0" width="46" height="366" fill="var(--navy)"/>
    </svg>
    <div class="brand">
      <span class="brand-name">Ardenwell</span>
      <span class="brand-tagline">Building and Property Services</span>
    </div>
    <div class="person">
      <p class="person-name">Duncan <span class="surname">Ferris</span></p>
      <p class="person-role">Director</p>
      <ul class="contact-list">
        <li>
          <svg viewBox="0 0 24 24" aria-hidden="true"><path d="M6.6 10.8a15.1 15.1 0 0 0 6.6 6.6l2.2-2.2a1 1 0 0 1 1-.25 11.4 11.4 0 0 0 3.6.57 1 1 0 0 1 1 1V20a1 1 0 0 1-1 1A17 17 0 0 1 3 4a1 1 0 0 1 1-1h3.5a1 1 0 0 1 1 1c0 1.25.2 2.45.57 3.57a1 1 0 0 1-.25 1z"/></svg>
          9518 2736
        </li>
        <li>
          <svg viewBox="0 0 24 24" aria-hidden="true"><path d="M2 5h20v14H2zm2 2v.5l8 5 8-5V7zm0 2.9V17h16V9.9l-8 5z"/></svg>
          dunardenwell@mailbox-example.com
        </li>
      </ul>
      <address class="address">
        Level 17, 82 Harlow Street<br>
        MERRIDALE<br>
        Melbourne, Vic 3094
      </address>
    </div>
  </section>

</main>
</body>
</html>
```